Quarrowby Roofing Business Card

Need a business card with the logo that was designed here

Contact Information for Business Card

Name, Title, Phone, Email, Website, Company name

```html
<!DOCTYPE html>
<html lang="en">
<head>
<meta charset="utf-8">
<title>Quarrowby Roofing Business Card</title>
<link rel="stylesheet" href="https://fonts.googleapis.com/css2?family=Arimo:wght@400;700&display=swap">
<style>
  :root {
    --stage: #3b3b3b;
    --card: #ffffff;
    --brand-blue: #2a78c8;
    --ink-grey: #6d6d6d;
    --rule-grey: #d4d4d4;
  }
  * { margin: 0; padding: 0; box-sizing: border-box; }
  html, body {
    width: 1200px;
    height: 689px;
    overflow: hidden;
    background: var(--stage);
    font-family: "Arimo", Arial, sans-serif;
  }
  .canvas {
    position: relative;
    width: 1200px;
    height: 689px;
    display: flex;
    align-items: center;
    justify-content: center;
    gap: 40px;
  }
  .card {
    position: relative;
    width: 520px;
    height: 297px;
    background: var(--card);
    border-radius: 22px;
    box-shadow: 0 10px 30px rgba(0,0,0,0.35);
    overflow: hidden;
  }
  .wordmark {
    display: flex;
    align-items: center;
    gap: 10px;
    color: var(--brand-blue);
    font-weight: 700;
    white-space: nowrap;
  }
  .wordmark__square {
    width: 14px;
    height: 14px;
    background: var(--brand-blue);
    flex: none;
  }
  .card--front {
    display: flex;
    align-items: center;
    justify-content: center;
  }
  .card--front .wordmark { font-size: 34px; }
  .card--front .wordmark__square { width: 20px; height: 20px; }

  .card--back .wordmark {
    position: absolute;
    left: 32px;
    top: 158px;
    font-size: 19px;
    gap: 7px;
  }
  .card--back .wordmark__square { width: 11px; height: 11px; }
  .divider {
    position: absolute;
    left: 262px;
    top: 40px;
    width: 1px;
    height: 220px;
    background: linear-gradient(to bottom, rgba(212,212,212,0), var(--rule-grey) 30%, var(--rule-grey) 70%, rgba(212,212,212,0));
  }
  .contact {
    position: absolute;
    left: 286px;
    top: 58px;
    right: 16px;
    color: var(--ink-grey);
    font-size: 12.5px;
    line-height: 1.35;
  }
  .contact__name {
    color: var(--brand-blue);
    font-weight: 700;
    font-size: 21px;
    line-height: 1.1;
  }
  .contact__title { font-size: 12px; margin-bottom: 14px; }
  .contact__address { margin-bottom: 12px; }
  .contact__list { list-style: none; }
  .contact__list li {
    display: flex;
    align-items: center;
    gap: 8px;
    white-space: nowrap;
  }
  .contact__icon { width: 11px; height: 11px; flex: none; fill: var(--brand-blue); }
</style>
</head>
<body>
<main class="canvas">
  <section class="card card--front">
    <div class="wordmark"><span class="wordmark__square"></span>Quarrowby Roofing</div>
  </section>

  <section class="card card--back">
    <div class="wordmark"><span class="wordmark__square"></span>Quarrowby Roofing</div>
    <div class="divider"></div>
    <div class="contact">
      <p class="contact__name">Dana Whitcombe</p>
      <p class="contact__title">President</p>
      <p class="contact__address">412 Harbor Ridge Road<br>Halden, Canada 58210</p>
      <ul class="contact__list">
        <li>
          <svg class="contact__icon" viewBox="0 0 24 24"><path d="M6.6 10.8a15.1 15.1 0 0 0 6.6 6.6l2.2-2.2c.3-.3.7-.4 1-.2 1.1.4 2.3.6 3.6.6.6 0 1 .4 1 1V20c0 .6-.4 1-1 1A17 17 0 0 1 3 4c0-.6.4-1 1-1h3.5c.6 0 1 .4 1 1 0 1.3.2 2.5.6 3.6.1.3 0 .7-.2 1z"/></svg>
          555-218-4407
        </li>
        <li>
          <svg class="contact__icon" viewBox="0 0 24 24"><path d="M7 1h10a2 2 0 0 1 2 2v18a2 2 0 0 1-2 2H7a2 2 0 0 1-2-2V3a2 2 0 0 1 2-2zm0 3v14h10V4zm5 15.5a1.2 1.2 0 1 0 0 2.4 1.2 1.2 0 0 0 0-2.4z"/></svg>
          555-218-4419
        </li>
        <li>
          <svg class="contact__icon" viewBox="0 0 24 24"><path d="M2 5h20v14H2zm2 2v.5l8 5 8-5V7zm0 2.8V17h16V9.8l-8 5z"/></svg>
          hello@quarrowbyroofing.com
        </li>
        <li>
          <svg class="contact__icon" viewBox="0 0 24 24"><path d="M12 2a10 10 0 1 0 0 20 10 10 0 0 0 0-20zm6.9 9h-3a15 15 0 0 0-1.3-5.6A8 8 0 0 1 18.9 11zM12 4c.9 1.2 1.8 3.6 1.9 7h-3.8C10.2 7.6 11.1 5.2 12 4zM9.4 5.4A15 15 0 0 0 8.1 11h-3a8 8 0 0 1 4.3-5.6zM5.1 13h3a15 15 0 0 0 1.3 5.6A8 8 0 0 1 5.1 13zM12 20c-.9-1.2-1.8-3.6-1.9-7h3.8c-.1 3.4-1 5.8-1.9 7zm2.6-1.4a15 15 0 0 0 1.3-5.6h3a8 8 0 0 1-4.3 5.6z"/></svg>
          www.quarrowbyroofing.com
        </li>
      </ul>
    </div>
  </section>
</main>
</body>
</html>
```